Product Introduction Brochure

Brochure to introduce our mid/high end lighting products to potential wholesalers / Disrtibutors / Retailers. To be mainly graphical but will contain some text also. The purpose of the brochure will be to get potential customers to find out more either by calling us or to visit our website. The brochure should be of A3 size folded in half to an A4. Front page should be mainly logo and name, inner 2 pages should showcase some of the products we can supply together with some text (to be supplied, please use filler text in the initial design), then the back page containing our contact details. The products are lights, floor lamps and table lamps. I have attached a number of images, as well as our company logo. I would prefer the design to be on a black background, however this is not critical
Target Market(s)
Retailer, distribution and wholesale buyers
Interior design consultants and specifiers
Industry/Entity Type
Product
Look and feel
Each slider illustrates characteristics of the customer's brand and the style your logo design should communicate.

```html
<!DOCTYPE html>
<html lang="en">
<head>
<meta charset="utf-8">
<title>Title Hentem Quibus — Lumora</title>
<link rel="stylesheet" href="https://fonts.googleapis.com/css2?family=Barlow:wght@300;400;500&display=swap">
<style>
  :root {
    --page-bg: #000000;
    --title-ink: #f4f4f4;
    --subtitle-ink: #a9a9a9;
    --product-light: #f2f1ee;
    --product-mid: #cfcdca;
    --product-shade: #5a5958;
    --brand-green: #3f9a3a;
    --brand-ink: #ffffff;
  }
  html, body {
    margin: 0;
    padding: 0;
    width: 849px;
    height: 1200px;
    overflow: hidden;
    background: var(--page-bg);
  }
  .cover {
    position: relative;
    width: 849px;
    height: 1200px;
    background: var(--page-bg);
    font-family: "Barlow", Arial, sans-serif;
    overflow: hidden;
  }
  .cover__title {
    position: absolute;
    left: 57px;
    top: 128px;
    margin: 0;
    font-weight: 300;
    font-size: 40px;
    letter-spacing: 1.5px;
    color: var(--title-ink);
    line-height: 1;
  }
  .cover__subtitle {
    position: absolute;
    left: 58px;
    top: 188px;
    margin: 0;
    font-weight: 400;
    font-size: 15px;
    letter-spacing: 1.6px;
    color: var(--subtitle-ink);
    line-height: 1;
  }
  .cover__product {
    position: absolute;
    left: 198px;
    top: 255px;
    width: 651px;
    height: 863px;
    background:
      radial-gradient(ellipse 62% 52% at 72% 46%, var(--product-light) 0%, var(--product-mid) 45%, var(--product-shade) 72%, var(--page-bg) 100%);
  }
  .brand {
    position: absolute;
    left: 51px;
    top: 1082px;
    display: flex;
    align-items: center;
    gap: 14px;
  }
  .brand__mark {
    width: 48px;
    height: 48px;
    background: var(--brand-green);
  }
  .brand__name {
    font-weight: 500;
    font-size: 40px;
    color: var(--brand-ink);
    line-height: 1;
  }
</style>
</head>
<body>
  <main class="cover">
    <h1 class="cover__title">TITLE HENTEM QUIBUS</h1>
    <p class="cover__subtitle">ACID QUAM QUOD MOLECAB</p>
    <div class="cover__product" role="img" aria-label="Photograph of a white ribbed pendant lamp shade lit against black"></div>
    <div class="brand">
      <span class="brand__mark"></span>
      <span class="brand__name">Lumora</span>
    </div>
  </main>
</body>
</html>
```